Pelin Thai Massage Double Sided Flyer Luxury

I require a double sided flyer
we are a Thai Massage Spa
Would like gold, deep purple and bronze colours
Something eye catching and looks professional

```html
<!DOCTYPE html>
<html lang="en">
<head>
<meta charset="utf-8">
<title>Pelin Thai Massage – Double Sided Flyer</title>
<link rel="stylesheet" href="https://fonts.googleapis.com/css2?family=Open+Sans:wght@400;600;700&family=Oswald:wght@600;700&display=swap">
<style>
  :root {
    --purple: #861b7b;
    --purple-deep: #6e1466;
    --gold: #d19a1c;
    --gold-light: #f3c232;
    --bronze: #a4680f;
    --ink: #2a2a2a;
    --paper: #ffffff;
    --backdrop: #ececec;
    --heading: "Oswald", "Arial Narrow", sans-serif;
    --body: "Open Sans", Arial, sans-serif;
  }
  * { box-sizing: border-box; margin: 0; padding: 0; }
  html, body { width: 1200px; height: 800px; overflow: hidden; background: var(--backdrop); }
  .canvas { position: relative; width: 1200px; height: 800px; }
  .flyer-side {
    position: absolute; top: 20px; width: 392px; height: 760px;
    background: var(--paper); overflow: hidden;
    font-family: var(--body); color: var(--ink);
  }
  .flyer-side--front { left: 196px; }
  .flyer-side--back { left: 611px; }
  .flyer-shapes { position: absolute; inset: 0; width: 392px; height: 760px; }

  .contact-list {
    position: absolute; top: 8px; left: 255px; list-style: none;
    font-size: 7.5px; line-height: 16.5px; color: #fff;
  }
  .contact-list b { display: inline-block; width: 16px; font-weight: 700; }

  .section-title {
    position: absolute; left: 0; width: 100%; text-align: center;
    font-family: var(--heading); font-weight: 700; color: var(--purple);
    text-transform: uppercase; letter-spacing: 0.2px;
  }
  .massages-title { top: 343px; font-size: 23px; line-height: 30px; }
  .intro-copy {
    position: absolute; left: 0; width: 100%; text-align: center;
    font-size: 13px; line-height: 19px; padding: 0 16px;
  }
  .massages-copy { top: 378px; font-size: 12px; padding: 0 22px; }

  .treatment-thumb {
    position: absolute; top: 456px; width: 99px; height: 99px; border-radius: 50%;
    background: linear-gradient(135deg, var(--bronze), var(--gold-light) 45%, var(--gold) 60%, var(--bronze));
    padding: 8px;
  }
  .treatment-thumb span { display: block; width: 100%; height: 100%; border-radius: 50%; }
  .thumb-stones { left: 27px; }
  .thumb-stones span { background: radial-gradient(circle at 40% 60%, #d89a6e, #7a4a2e); }
  .thumb-oils { left: 147px; }
  .thumb-oils span { background: radial-gradient(circle at 50% 55%, #c9a23a, #b9cbd6 70%); }
  .thumb-hands { left: 269px; }
  .thumb-hands span { background: radial-gradient(circle at 50% 60%, #e9c9b2, #8fb0c4 75%); }

  .feature-badge {
    position: absolute; top: 567px; width: 125px; height: 125px;
    display: flex; align-items: center; justify-content: center; text-align: center;
    color: #fff; font-weight: 700; font-size: 11.5px; line-height: 15px; text-transform: uppercase;
  }
  .feature-badge::before, .feature-badge::after {
    content: ""; position: absolute; left: 50%; top: 50%;
    transform: translate(-50%, -50%) rotate(45deg);
  }
  .feature-badge::before { width: 88px; height: 88px; background: var(--purple); border-radius: 6px; }
  .feature-badge::after { width: 80px; height: 80px; border: 1px dashed rgba(255,255,255,0.9); border-radius: 4px; }
  .feature-badge p { position: relative; z-index: 1; }
  .badge-hours { left: 63px; }
  .badge-vouchers { left: 202px; }

  .brand-mark {
    position: absolute; top: 170px; left: 22px; width: 150px; text-align: center;
  }
  .brand-mark i {
    display: block; width: 54px; height: 54px; margin: 0 auto 4px; border-radius: 50%;
    border: 2px solid var(--gold-light);
  }
  .brand-mark span { font-size: 12px; color: var(--gold-light); font-weight: 400; }

  .welcome-title {
    position: absolute; top: 246px; left: 0; width: 100%; text-align: center;
    font-family: var(--heading); font-weight: 700; font-size: 47px; line-height: 56px;
    color: var(--purple);
  }
  .welcome-copy { top: 322px; font-size: 12.6px; }
  .craft-copy { top: 386px; font-size: 12.6px; padding: 0 10px; }

  .service-title { font-size: 21px; line-height: 26px; }
  .deep-title { top: 487px; }
  .floor-title { top: 638px; }
  .price-line {
    position: absolute; left: 0; width: 100%; text-align: center;
    font-weight: 700; font-size: 14.5px; line-height: 20px;
  }
  .price-note {
    position: absolute; left: 0; width: 100%; text-align: center;
    font-size: 12.6px; line-height: 19px; padding: 0 40px;
  }
</style>
</head>
<body>
<main class="canvas">

  <section class="flyer-side flyer-side--front">
    <svg class="flyer-shapes" viewBox="0 0 392 760">
      <defs>
        <linearGradient id="goldFront" x1="0" y1="0" x2="1" y2="0">
          <stop offset="0" stop-color="#a4680f"/>
          <stop offset="0.35" stop-color="#d19a1c"/>
          <stop offset="0.7" stop-color="#f3c232"/>
          <stop offset="1" stop-color="#a4680f"/>
        </linearGradient>
        <linearGradient id="photoWarm" x1="0" y1="0" x2="1" y2="1">
          <stop offset="0" stop-color="#f6d98a"/>
          <stop offset="0.5" stop-color="#efb987"/>
          <stop offset="1" stop-color="#e1a06a"/>
        </linearGradient>
      </defs>
      <path d="M392 0 V298 C380 330 340 340 300 336 C240 328 190 285 140 274 C80 282 20 330 0 397 V0 Z" fill="var(--purple)"/>
      <g role="img" aria-label="Photo of a woman relaxing during a back massage">
        <path d="M0 0 H392 V194 C370 260 320 300 260 285 C200 265 150 225 90 218 C60 215 30 225 0 254 Z" fill="url(#photoWarm)"/>
      </g>
      <path d="M392 194 C370 260 320 300 260 285 C200 265 150 225 90 218 C60 215 30 225 0 254 L0 304 C40 270 100 258 150 272 C200 290 250 315 300 323 C330 330 370 320 392 276 Z" fill="url(#goldFront)"/>
      <path d="M0 280 C35 245 80 237 120 242 C180 252 230 295 290 305 C340 312 380 280 392 235" fill="none" stroke="#fff" stroke-width="1.3" stroke-dasharray="7 5"/>
      <path d="M0 0 H392 V192 C340 97 240 32 0 0 Z" fill="var(--purple)"/>
      <path d="M0 2 C240 34 340 99 392 194" fill="none" stroke="url(#goldFront)" stroke-width="4"/>
      <path d="M0 650 C8 700 30 738 70 760 H0 Z" fill="url(#goldFront)"/>
      <path d="M4 665 C12 705 28 735 50 758" fill="none" stroke="#fff" stroke-width="1.2" stroke-dasharray="6 5"/>
      <path d="M160 760 C210 725 255 702 300 700 C345 700 378 728 392 748 V760 Z" fill="url(#goldFront)"/>
      <path d="M185 760 C225 732 262 714 300 712 C338 712 368 732 386 756" fill="none" stroke="#fff" stroke-width="1.2" stroke-dasharray="6 5"/>
    </svg>

    <ul class="contact-list">
      <li><b>P:</b>0113 496 0728</li>
      <li><b>A:</b>14 Willow Row Leeds LS9 2QT</li>
      <li><b>W:</b>www.pelinthaimassage.co.uk</li>
    </ul>

    <h2 class="section-title massages-title">Massages</h2>
    <p class="intro-copy massages-copy">Restore balance. Revive your senses. Discover all the ways Pelin Thai Massage can breathe new life into your body and soul.</p>

    <div class="treatment-thumb thumb-stones"><span role="img" aria-label="Photo of hot stones placed on a back"></span></div>
    <div class="treatment-thumb thumb-oils"><span role="img" aria-label="Photo of a golden statue with towels and oils"></span></div>
    <div class="treatment-thumb thumb-hands"><span role="img" aria-label="Photo of hands massaging a back"></span></div>

    <div class="feature-badge badge-hours"><p>Open<br>7 days a week</p></div>
    <div class="feature-badge badge-vouchers"><p>Gift<br>vouchers<br>available</p></div>
  </section>

  <section class="flyer-side flyer-side--back">
    <svg class="flyer-shapes" viewBox="0 0 392 760">
      <defs>
        <linearGradient id="goldBack" x1="0" y1="0" x2="1" y2="0">
          <stop offset="0" stop-color="#a4680f"/>
          <stop offset="0.35" stop-color="#d19a1c"/>
          <stop offset="0.7" stop-color="#f3c232"/>
          <stop offset="1" stop-color="#a4680f"/>
        </linearGradient>
        <linearGradient id="photoSpa" x1="0" y1="0" x2="1" y2="1">
          <stop offset="0" stop-color="#e9efe2"/>
          <stop offset="0.5" stop-color="#efe4d6"/>
          <stop offset="1" stop-color="#dcc39c"/>
        </linearGradient>
      </defs>
      <path d="M0 0 H392 V205 C370 235 330 240 290 230 C230 215 170 165 110 158 C60 152 20 190 0 240 Z" fill="var(--purple)"/>
      <g role="img" aria-label="Photo of a mortar with fresh herbs and bottles of massage oil">
        <path d="M0 0 H392 V110 C380 170 340 195 290 192 C230 188 170 140 110 135 C60 130 20 160 0 200 Z" fill="url(#photoSpa)"/>
      </g>
      <path d="M0 190 C20 150 60 125 105 125 C170 125 230 180 290 185 C345 190 380 150 392 85 L392 170 C375 205 340 215 290 210 C230 205 170 150 110 145 C60 140 20 175 0 215 Z" fill="url(#goldBack)"/>
      <path d="M0 203 C20 160 60 135 107 135 C170 137 230 193 290 197 C345 200 385 165 392 128" fill="none" stroke="#fff" stroke-width="1.3" stroke-dasharray="7 5"/>
      <path d="M0 680 C10 715 25 740 45 760 H0 Z" fill="url(#goldBack)"/>
      <path d="M4 692 C12 722 24 744 36 758" fill="none" stroke="#fff" stroke-width="1.2" stroke-dasharray="6 5"/>
      <path d="M200 760 C240 735 275 720 310 720 C345 722 375 740 392 755 V760 Z" fill="url(#goldBack)"/>
      <path d="M225 760 C258 742 285 732 312 732 C340 733 365 745 384 758" fill="none" stroke="#fff" stroke-width="1.2" stroke-dasharray="6 5"/>
    </svg>

    <div class="brand-mark"><i></i><span>Pelin Thai Massage</span></div>

    <h1 class="welcome-title">Welcome to Luxury</h1>
    <p class="intro-copy welcome-copy">Set in the heart of Roundhay, Pelin Thai Massage will allow you to immerse yourself in a place where your wellbeing and rejuvenation is at the centre of what we do.</p>
    <p class="intro-copy craft-copy">Using Thai traditions, our highly trained therapists offer revitalising body treatments with their deep tissue massage techniques. In their hands, you will see and feel immediate results.</p>

    <h2 class="section-title service-title deep-title">Deep Tissue Massage</h2>
    <p class="price-line" style="top:518px">60 minutes £45</p>
    <p class="price-note" style="top:542px">Oil massage personalised, light to firm pressure</p>
    <p class="price-line" style="top:575px">90 minutes £55</p>
    <p class="price-note" style="top:599px">Oil massage, medium to firm pressure</p>

    <h2 class="section-title service-title floor-title">Thai Floor Tradtional Massage</h2>
    <p class="price-line" style="top:668px">60 minutes £45</p>
    <p class="price-note" style="top:692px">Dry massage, medium to firm pressure applying stretching technique</p>
  </section>

</main>
</body>
</html>
```